Digital Marketing Consultant Needs a Business Card Design

I need a business card to brand myself - I'm a digital marketing consultant, and I do web design, SEO, lead generation, social media, etc. I'm overhauling my website (CorinneHalvorsk.com) and just had a snazzy new logo made.

I like the combo of yellow & gray - I find it eye-catching, upbeat and techie. The exact colors of yellow and gray that I like are #F6BF27 and #6D6D6D. But I'm open to suggestions and other color combinations!

I plan on printing the card using some high-end printing techniques that will ensure the card stands out - either really thick cards with colored edges, or spot UV. Not sure which yet, so if you want to incorporate that into your design, that'd be great!

I'm looking for a clean and modern design, but something that will really stand out when paired with 'fancy' printing.

Target Market(s)

Small and medium-sized business owners.

Industry/Entity Type

Printing

Contact Information for Business Card

Corinne Halvorsk
Digital Marketing
Call or Text: 850-555-0927
Corinne@CorinneHalvorsk.com
www.CorinneHalvorsk.com
@QPZ47 on Chirpline

Font styles to use
Serif
Sans Serif

Requirements
Must have
• My logo, my contact information, and my "company colors" - #F6BF27 and #6D6D6D.
Nice to have
• If there's room to mention all the things that I do:
• Social Media, Web Design, SEO, Lead Generation, Conversion Funnels, PPC
• (don't add if it makes the card cluttered)

```html
<!DOCTYPE html>
<html lang="en">
<head>
<meta charset="utf-8">
<title>Corinne Halvorsk – Business Card</title>
<link href="https://fonts.googleapis.com/css2?family=Cormorant+Garamond:wght@500&family=Roboto:wght@300;400&display=swap" rel="stylesheet">
<style>
  :root {
    --yellow: #F6BF27;
    --gray: #6D6D6D;
    --gray-light: #a9a9a9;
    --rule: #cfcfcf;
    --card: #fbfbfb;
    --backdrop: #ecebe8;
  }
  * { box-sizing: border-box; margin: 0; padding: 0; }
  html, body { width: 1200px; height: 885px; overflow: hidden; }
  body {
    background: var(--backdrop);
    font-family: "Roboto", Arial, sans-serif;
    display: flex;
    align-items: center;
    justify-content: center;
    gap: 40px;
  }
  .card {
    position: relative;
    width: 540px;
    height: 309px;
    background: var(--card);
    border-radius: 18px;
    box-shadow: 0 2px 0 #e0e0e0, 0 4px 0 #d4d4d4, 0 6px 0 #e0e0e0, 0 14px 30px rgba(0,0,0,.18);
    overflow: hidden;
  }

  /* Front */
  .front .mark {
    position: absolute; left: 30px; top: 96px; width: 170px;
    display: flex; flex-direction: column; align-items: center; gap: 14px;
  }
  .mark-square {
    width: 70px; height: 70px; border: 6px solid var(--gray-light);
  }
  .mark-name {
    font-family: "Cormorant Garamond", Georgia, serif;
    font-weight: 500; font-size: 22px; color: var(--gray);
    text-align: center; line-height: 1.1;
  }
  .front .divider {
    position: absolute; left: 218px; top: 40px; width: 1px; height: 230px;
    background: linear-gradient(var(--card), var(--rule), var(--card));
  }
  .identity { position: absolute; left: 250px; top: 44px; }
  .identity .name { font-size: 27px; color: var(--yellow); font-weight: 400; }
  .identity .title { font-size: 16px; color: var(--gray); font-weight: 300; margin-top: 2px; }
  .contacts { position: absolute; left: 250px; top: 126px; list-style: none; }
  .contacts li {
    display: flex; align-items: center; gap: 10px;
    font-size: 13.5px; color: var(--gray); height: 26px;
  }
  .contacts svg { width: 17px; height: 17px; flex: none; }
  .socials { position: absolute; right: 22px; bottom: 22px; display: flex; gap: 6px; }
  .socials span { width: 20px; height: 20px; background: var(--gray-light); border-radius: 3px; }

  /* Back */
  .back .mark-square.small { position: absolute; left: 360px; top: 52px; width: 62px; height: 62px; border-width: 5px; }
  .back .wordmark {
    position: absolute; left: 40px; top: 132px;
    font-family: "Cormorant Garamond", Georgia, serif;
    font-weight: 500; font-size: 38px; letter-spacing: 2px; color: var(--gray);
  }
  .back .tagline {
    position: absolute; right: 40px; top: 180px;
    font-size: 12px; letter-spacing: 5px; color: var(--gray-light); font-weight: 300;
  }
  .back .rule { position: absolute; left: 40px; top: 206px; width: 180px; height: 1px; background: var(--rule); }
  .services {
    position: absolute; left: 40px; top: 220px;
    font-size: 14px; line-height: 1.45; color: var(--gray); font-weight: 300;
  }
</style>
</head>
<body>
  <section class="card front" aria-label="Card front">
    <div class="mark">
      <div class="mark-square"></div>
      <div class="mark-name">Corinne Halvorsk</div>
    </div>
    <div class="divider"></div>
    <div class="identity">
      <h1 class="name">Corinne Halvorsk</h1>
      <p class="title">Digital Marketing</p>
    </div>
    <ul class="contacts">
      <li>
        <svg viewBox="0 0 17 17"><rect width="17" height="17" rx="2" fill="var(--yellow)"/><path d="M5 4h2l1 3-1.3 1a6 6 0 0 0 2.3 2.3L10 9l3 1v2a1 1 0 0 1-1 1A8 8 0 0 1 4 5a1 1 0 0 1 1-1z" fill="#fff"/></svg>
        850-555-0927
      </li>
      <li>
        <svg viewBox="0 0 17 17"><rect width="17" height="17" rx="2" fill="var(--yellow)"/></svg>
        @QPZ47 on Chirpline
      </li>
      <li>
        <svg viewBox="0 0 17 17"><rect width="17" height="17" rx="2" fill="var(--yellow)"/><circle cx="8.5" cy="8.5" r="5" fill="none" stroke="#fff" stroke-width="1.3"/><path d="M3.5 8.5h10M8.5 3.5c-2.5 3-2.5 7 0 10M8.5 3.5c2.5 3 2.5 7 0 10" fill="none" stroke="#fff" stroke-width="1"/></svg>
        www.CorinneHalvorsk.com
      </li>
      <li>
        <svg viewBox="0 0 17 17"><rect width="17" height="17" rx="2" fill="var(--yellow)"/><rect x="3.5" y="5" width="10" height="7" fill="none" stroke="#fff" stroke-width="1.3"/><path d="M3.5 5l5 4 5-4" fill="none" stroke="#fff" stroke-width="1.3"/></svg>
        Corinne@CorinneHalvorsk.com
      </li>
    </ul>
    <div class="socials" aria-label="Social profiles"><span></span><span></span><span></span><span></span></div>
  </section>

  <section class="card back" aria-label="Card back">
    <div class="mark-square small"></div>
    <h2 class="wordmark">CORINNE HALVORSK</h2>
    <p class="tagline">digital marketing</p>
    <div class="rule"></div>
    <p class="services">Social Media, Web Design, SEO, Lead Generation<br>Conversion Funnels, PPC</p>
  </section>
</body>
</html>
```